Tiling Service Contractor For Custom Van Design.

I am a independent Tiling Contractor
All types of tiles, Ceramic, Porcelain, Natural Stone,
I need my van to be designed to give maximum advertising to generate more buisness and leads. I am in 2 minds, weather to have something brief and professional or go for the full wrap, I am open to all designs, you don necessary have to use my logo, as i have seen other independent contractors
Domestic & Commercial
Walls & Floor Tiler
Complete Bathroom Installations
www.cresmoraweb.ie
Email: info@cresmoraweb.ie

Target Market(s)

Everybody, house owners, other contractors

Industry/Entity Type

construction, tiling, building

Requirements
Must have
• contact info

```html
<!DOCTYPE html>
<html lang="en">
<head>
<meta charset="utf-8">
<title>Cresmora Tiling – Van Livery</title>
<link rel="stylesheet" href="https://fonts.googleapis.com/css2?family=Anton&family=Arimo:wght@400;700&family=Montserrat:wght@900&display=swap">
<style>
  :root {
    --backdrop: #eceef1;
    --van-white: #ffffff;
    --van-edge: #c9cdd2;
    --trim-black: #1b1b1d;
    --glass: #2e3236;
    --band-black: #050505;
    --band-red: #6b0000;
    --band-red-light: #b3060f;
    --band-gold: #a58c3e;
    --headline-red: #c0000c;
    --ink: #111111;
    --steel: #9aa0a6;
  }
  html, body {
    margin: 0;
    padding: 0;
    width: 1200px;
    height: 737px;
    overflow: hidden;
    background: var(--backdrop);
  }
  .livery {
    display: block;
    width: 1200px;
    height: 737px;
  }
  .van-body { fill: var(--van-white); stroke: var(--van-edge); stroke-width: 4; }
  .van-trim { fill: var(--trim-black); }
  .van-glass { fill: var(--glass); }
  .van-panel-line { stroke: var(--van-edge); stroke-width: 4; fill: none; }
  .wheel-tyre { fill: var(--trim-black); }
  .wheel-hub { fill: var(--steel); }
  .band-black { fill: var(--band-black); }
  .band-red { fill: var(--band-red); }
  .band-red-edge { fill: var(--band-red-light); }
  .band-gold { fill: var(--band-gold); }
  .tile-sample { stroke: var(--band-black); stroke-width: 14; }
  .tile-marble { fill: #e4e2de; }
  .tile-amber { fill: #f2a932; }
  .tile-slate { fill: #9c7a6c; }
  .side-word {
    font-family: "Montserrat", sans-serif;
    font-weight: 900;
    font-size: 178px;
    fill: var(--van-white);
  }
  .band-caps {
    font-family: "Arimo", sans-serif;
    font-weight: 700;
    font-size: 42px;
    fill: var(--van-white);
  }
  .band-small {
    font-family: "Arimo", sans-serif;
    font-weight: 400;
    font-size: 30px;
    fill: var(--van-white);
  }
  .brand-name {
    font-family: "Montserrat", sans-serif;
    font-weight: 900;
    font-size: 54px;
    fill: var(--ink);
  }
  .brand-mark { fill: none; stroke: var(--ink); stroke-width: 8; }
  .services {
    font-family: "Anton", sans-serif;
    font-size: 80px;
    fill: var(--headline-red);
    text-anchor: middle;
  }
  .contact-email {
    font-family: "Arimo", sans-serif;
    font-size: 36px;
    fill: var(--van-white);
  }
  .contact-web {
    font-family: "Arimo", sans-serif;
    font-weight: 700;
    font-size: 44px;
    fill: var(--van-white);
  }
  .door-name {
    font-family: "Montserrat", sans-serif;
    font-weight: 900;
    font-size: 15px;
    fill: var(--ink);
    text-anchor: middle;
  }
</style>
</head>
<body>
<svg class="livery" viewBox="0 0 2462 1512" xmlns="http://www.w3.org/2000/svg" aria-label="Cresmora Tiling van side livery">
  <path class="van-body" d="M150,330 Q160,305 230,302 L1360,308 Q1700,318 1900,470 L2080,640 Q2250,690 2300,760 L2340,960 L2340,1080 L2180,1100 Q2150,960 1985,950 Q1830,960 1800,1110 L740,1120 Q720,960 555,950 Q400,960 370,1100 L120,1080 L110,880 L100,470 Q110,350 150,330 Z"/>
  <path class="van-glass" d="M1440,370 L1690,372 Q1780,380 1880,480 L2050,690 L1470,660 Q1440,655 1440,630 Z"/>
  <path class="van-panel-line" d="M1360,310 L1360,1115 M1940,680 L1930,1090"/>

  <path class="band-black" d="M218,305 L330,305 L505,905 L390,945 L218,915 Z"/>
  <path class="band-red-edge" d="M360,305 L372,305 L620,1000 L608,1000 Z"/>
  <path class="band-red" d="M372,305 L465,305 L700,880 Q722,925 790,928 L1850,975 L1800,1100 L740,1082 Q650,1070 625,1000 Z"/>
  <path class="band-gold" d="M480,305 L565,305 L830,740 Q855,775 925,780 L2285,895 L2255,940 L790,905 Q735,900 712,858 Z"/>

  <circle class="tile-sample tile-marble" cx="430" cy="445" r="75" role="img" aria-label="Marble tile sample"/>
  <circle class="tile-sample tile-amber" cx="470" cy="628" r="75" role="img" aria-label="Amber ceramic tile sample"/>
  <circle class="tile-sample tile-slate" cx="550" cy="810" r="75" role="img" aria-label="Natural stone tile sample"/>

  <text class="side-word" transform="translate(250,412) rotate(90)" textLength="432" lengthAdjust="spacingAndGlyphs">TILING</text>
  <text class="band-caps" transform="translate(530,338) rotate(60)">COMPLETE</text>
  <text class="band-small" transform="translate(662,570) rotate(58)">Bathroom Installations</text>

  <rect class="brand-mark" x="712" y="385" width="90" height="90"/>
  <text class="brand-name" x="835" y="452" textLength="485" lengthAdjust="spacingAndGlyphs">CRESMORA TILING</text>
  <text class="services" x="1068" y="562">DOMESTIC</text>
  <text class="services" x="1072" y="637">&amp; COMMERCIAL</text>

  <text class="contact-email" transform="translate(950,862) rotate(3)">info@cresmoraweb.ie</text>
  <text class="contact-web" transform="translate(1418,885) rotate(3)">www.cresmoraweb.ie</text>

  <rect class="brand-mark" x="1690" y="705" width="80" height="80"/>
  <text class="door-name" x="1730" y="822">CRESMORA TILING</text>

  <path class="van-trim" d="M845,955 L1350,975 L1350,1005 L860,1000 Q840,990 845,955 Z"/>
  <path class="van-trim" d="M1365,975 L1690,1000 L1705,1035 L1365,1025 Z"/>
  <path class="van-trim" d="M110,1000 L370,1010 L360,1090 L120,1080 Z"/>
  <path class="van-trim" d="M2180,990 L2340,980 L2340,1080 L2180,1100 Z"/>

  <circle class="wheel-tyre" cx="555" cy="1115" r="165"/>
  <circle class="wheel-hub" cx="555" cy="1115" r="100"/>
  <circle class="wheel-tyre" cx="1985" cy="1105" r="165"/>
  <circle class="wheel-hub" cx="1985" cy="1105" r="100"/>
</svg>
</body>
</html>
```